Commercial Real Estate for Lease Listing Flyer

I am looking to put together a flyer for our available office space in our building. It needs to look professional and it will be standard sized 8.5 x 11 and double sided. Full color as well. This flyer will need to be able to be put in a PDF and a picture file that can be embedded in an email. I have included pictures, logo, and a Word document with the information you should need. Also, I included a bunch of SAMPLE leasing flyers that you can get ideas from. The floor plan is also included in here. I want it specifically noted that the top suite is Suite 100 and the bottom suite is 120. And list their size as well. I will be reviewing all designs very quickly, so be sure to check the comments.

Requirements
Must have
• Please refer to these links for additional photos:
• "Twilight 1.jpg" at: https://docs.vellorashare.net/v/view/3f1c7a20-5b9e-4d1a-8c3f-7e2b9a4d6c11
• Twilight 2_straightened.jpg" at: https://docs.vellorashare.net/v/view/8a4e2d61-1c7b-4f3e-9b5a-2d6f8e1c4a72
• "Twilight 3.jpg" at: https://docs.vellorashare.net/v/view/5d9b1e73-6f2a-4c8d-a3e1-9f4c7b2e5d83
• "Twilight 4.jpg" at: https://docs.vellorashare.net/v/view/2c7f4a95-8e1d-4b6c-b2f4-1a3e9d7c8f04
• "Twilight 5.jpg" at: https://docs.vellorashare.net/v/view/9e3a6c18-4d7f-4a2b-8c5e-6b1f2a9d3e15
• "Twilight 6.jpg" at: https://docs.vellorashare.net/v/view/4b8d2f36-7a1e-4e9c-a6d3-3c5b8e2f7a26
• "Twilight 7.jpg" at: https://docs.vellorashare.net/v/view/7f2e5b49-3c8a-4d1f-b9e2-8a4d1c6b9f37
• "Twilight 8.jpg" at: https://docs.vellorashare.net/v/view/1a6c9d52-2b4e-4f7a-8d1c-5e7a3b8c2d48
• "Twilight 9.jpg" at: https://docs.vellorashare.net/v/view/6d4f1a83-9e2c-4b5d-a7f8-4c2e6d1a5b59
• "Twilight 10.jpg" at: https://docs.vellorashare.net/v/view/3e8b7c14-5f9d-4a6e-b3c2-7d9f4e8b1c60
• "Twilight 11.jpg" at: https://docs.vellorashare.net/v/view/8c5a3e27-1d6b-4e8f-9a4d-2f1c7a5e3d71

```html
<!DOCTYPE html>
<html lang="en">
<head>
<meta charset="utf-8">
<title>Kestrel Road Centre – Office Space for Lease</title>
<link href="https://fonts.googleapis.com/css2?family=Cinzel:wght@500&family=Kristi&family=Source+Sans+3:wght@300;400;600;700&display=swap" rel="stylesheet">
<style>
  :root{
    --brand-blue:#0c4f95;
    --panel-grey:#7b7c7e;
    --plan-bg:#ededed;
    --ink:#3b3b3b;
    --page:#ffffff;
    --backdrop:#d9d9d9;
    --caption-bg:rgba(40,40,40,.72);
  }
  *{box-sizing:border-box;margin:0;padding:0}
  html,body{width:1200px;height:925px;overflow:hidden}
  body{background:var(--backdrop);font-family:"Source Sans 3",Arial,sans-serif;color:var(--ink);position:relative}
  .sheet{position:absolute;top:137px;width:470px;height:608px;background:var(--page);box-shadow:0 4px 14px rgba(0,0,0,.25);overflow:hidden}
  .sheet--front{left:94px}
  .sheet--back{left:621px}
  .abs{position:absolute}

  .brand-name{color:var(--brand-blue);font-weight:600;text-transform:uppercase;line-height:1;text-align:center;white-space:nowrap}
  .brand-name span{display:block}
  .brand-name .big{font-size:23px;letter-spacing:3px;margin-right:-3px}
  .brand-name .small{font-size:10px;letter-spacing:3px;margin-right:-3px;margin-top:3px}

  .office-address{font-size:6.6px;line-height:10.5px;color:#555}

  .photo{position:absolute}
  .hero{left:0;top:86px;width:470px;height:236px;background:linear-gradient(180deg,#6b6258 0%,#8a7a66 45%,#b8b0a2 80%,#5d6e45 100%)}
  .hero-title{position:absolute;left:25px;top:100px;font-family:"Kristi",cursive;color:#fff;font-size:74px;line-height:1;white-space:nowrap;text-shadow:0 1px 3px rgba(0,0,0,.4)}
  .hero-address{position:absolute;left:0;bottom:0;width:235px;height:15px;background:var(--caption-bg);color:#fff;font-size:8px;line-height:15px;padding-left:20px;font-weight:300}

  .intro{left:19px;top:335px;width:196px;font-size:5.9px;line-height:7.4px}
  .intro h2{color:var(--brand-blue);font-size:8.5px;font-weight:700;line-height:10px}
  .intro .lead{font-weight:600;margin-bottom:4px}
  .intro p{margin-bottom:3.5px}
  .facts{display:flex;gap:22px;margin-top:8px}
  .facts ul{list-style:none;line-height:11.5px}

  .thumb{width:111px;height:88px}
  .thumb--1{left:237px;top:332px;background:linear-gradient(180deg,#6f88a8,#b9a98e 60%,#59604a)}
  .thumb--2{left:359px;top:332px;background:linear-gradient(180deg,#6f9ed0,#d8c7a6 60%,#6a7a52)}
  .thumb--3{left:237px;top:428px;background:linear-gradient(135deg,#8a5a3a,#c9b59a 55%,#6d5344)}
  .thumb--4{left:359px;top:428px;background:linear-gradient(135deg,#c8b48a,#6b4a36 60%,#3a3432)}

  .contact-band{left:0;top:526px;width:470px;height:71px;background:var(--brand-blue);color:#fff}
  .band-contact{position:absolute;left:19px;top:8px;font-size:6.6px;line-height:10px}
  .band-contact .name{font-weight:700;font-size:8px;margin-top:5px}
  .icon-line{display:flex;align-items:center;gap:3px}
  .icon-line svg{width:5px;height:5px}
  .suite-card{position:absolute;top:5px;width:130px;height:58px;border:1px solid #fff;text-align:center;padding:4px 6px}
  .suite-card h3{font-size:10px;font-weight:600;line-height:12px;margin-bottom:2px}
  .suite-card p{font-size:5.6px;line-height:7.2px}
  .suite-card--120{left:192px}
  .suite-card--100{left:331px}

  .title-block{left:17px;top:13px;width:289px;height:50px;background:var(--brand-blue);color:#fff;font-family:"Cinzel",serif;font-size:24px;line-height:50px;text-align:center;font-weight:500;white-space:nowrap}
  .spec-panel{background:var(--panel-grey);color:#fff;padding:12px 12px;font-weight:300;font-size:8.6px;line-height:13px}
  .spec-panel h3{font-weight:400;font-size:13px;line-height:16px;margin-bottom:3px}
  .spec-panel ul{list-style:none}
  .spec--120{left:317px;top:13px;width:140px;height:147px}
  .spec--100{left:17px;top:415px;width:140px;height:156px;padding-top:16px}
  .plan{background:var(--plan-bg)}
  .plan--120{left:317px;top:170px;width:140px;height:113px}
  .plan--100{left:17px;top:294px;width:140px;height:112px}
  .room--120{left:17px;top:73px;width:289px;height:210px;background:linear-gradient(180deg,#d9d3c4 0%,#c9a646 35%,#b99a45 60%,#8f8676 100%)}
  .room--100{left:167px;top:294px;width:290px;height:196px;background:linear-gradient(180deg,#e4dcc8 0%,#c9a85a 40%,#6b4b3a 70%,#3c3634 100%)}
  .caption{position:absolute;left:0;bottom:0;width:100%;height:21px;background:var(--caption-bg);color:#fff;font-size:8.5px;line-height:21px;text-align:right;padding-right:16px;font-weight:300}
  .back-contact{left:175px;top:508px;font-size:8.6px;line-height:11px;color:#555}
  .back-contact .name{color:var(--brand-blue);margin-top:3px}
  .back-contact .icon-line svg{width:6px;height:6px}
  .front-brand{left:18px;top:26px;width:126px}
  .back-brand{left:325px;top:515px;width:132px}
  .footer-rule{left:17px;top:580px;width:440px;height:13px;background:var(--brand-blue)}
</style>
</head>
<body>

<section class="sheet sheet--front">
  <div class="abs brand-name front-brand">
    <span class="big">Norvale</span><span class="small">Companies</span>
  </div>
  <div class="abs office-address" style="left:197px;top:34px">Corporate Headquarters:<br>4180 Kestrel Road, Suite 110<br>Palm Beach Gardens, FL 33418</div>
  <div class="abs office-address" style="left:328px;top:34px">Atlanta, Georgia Office:<br>275 Larkspur Parkway, Suite 4245<br>Cumming, GA 30041</div>

  <div class="photo hero" role="img" aria-label="Twilight photo of the building's arched columned entrance">
    <div class="hero-title">Office Space for Lease</div>
    <div class="hero-address">4180 Kestrel Road, Palm Beach Gardens, FL 33418</div>
  </div>

  <div class="abs intro">
    <h2>Kestrel Road Center</h2>
    <p class="lead">Two suites are available, 1,488 SF + 2,303 SF.</p>
    <p>The Kestrel Road Centre is a beautiful Class A building situation in the heart of Palm Beach Gardens but without the crazy boulevard traffic. Kestrel Road Centre is located directly on I-95 just off of Kestrel Road.</p>
    <p>The massive, new Brightwater development south entrance is being built across the street. The building is very convenient to restaurants, shopping, and every other trade needed.</p>
    <p>The suites are incredibly well appointed and move-in ready with custom oak doors and millwork, 10' ceilings, floor to ceiling windows.</p>
    <div class="facts">
      <ul>
        <li>• Building Size: 18,325 SF</li>
        <li>• Vacant SF: 3,791 SF</li>
        <li>• Occupancy: 79%</li>
        <li>• Rental Rate: $32.00/SF + electric</li>
        <li>• No extra operating expenses.</li>
      </ul>
      <ul>
        <li>Features &amp; Amenities:</li>
        <li>• Plenty of parking</li>
        <li>• On-site management</li>
        <li>• Some furniture available.</li>
      </ul>
    </div>
  </div>

  <div class="photo thumb thumb--1" role="img" aria-label="Building exterior with palm trees and parking lot"></div>
  <div class="photo thumb thumb--2" role="img" aria-label="Building exterior under blue sky with palm trees"></div>
  <div class="photo thumb thumb--3" role="img" aria-label="Interior lobby with chandelier and elevator"></div>
  <div class="photo thumb thumb--4" role="img" aria-label="Office meeting room with arched windows"></div>

  <div class="abs contact-band">
    <div class="band-contact">
      Very easy to show as landlord is in the building.<br>
      For leasing information, please contact:
      <div class="name">Dana Morrell</div>
      <div class="icon-line"><svg viewBox="0 0 10 10"><path d="M2 1l2 0 1 2-1.2 1a5 5 0 0 0 2.2 2.2L7 5l2 1v2a1 1 0 0 1-1 1A8 8 0 0 1 1 2a1 1 0 0 1 1-1z" fill="#fff"/></svg>561-555-0148</div>
      <div class="icon-line"><svg viewBox="0 0 10 10"><rect x="0.5" y="2" width="9" height="6" fill="#fff"/></svg>dana@norvalecompanies.com</div>
    </div>
    <div class="suite-card suite-card--120">
      <h3>SUITE 120</h3>
      <p>Available right now and is 1,488 SF with 1 large executive office, 2 smaller offices, a conference room, break room, and reception area.</p>
    </div>
    <div class="suite-card suite-card--100">
      <h3>SUITE 100</h3>
      <p>Available in February 2019, but could be vacated sooner. Suite 100 is 2,303 SF and has 6 offices, break room, reception area, and a very large meeting room.</p>
    </div>
  </div>
</section>

<section class="sheet sheet--back">
  <h1 class="abs title-block">Kestrel Road Centre</h1>

  <div class="abs spec-panel spec--120">
    <h3>SUITE 120</h3>
    <ul>
      <li>1,488 sq ft</li>
      <li>1 Large Executive Office</li>
      <li>2 Smaller Offices</li>
      <li>Conference Room</li>
      <li>Break Room</li>
      <li>Reception Area</li>
      <li>Plenty of parking</li>
      <li>On-site management</li>
    </ul>
  </div>

  <div class="photo room--120" role="img" aria-label="Empty executive office in Suite 120 with desk and tall windows">
    <div class="caption">SUITE 120 - AVAILABLE RIGHT NOW</div>
  </div>
  <div class="photo plan plan--120" role="img" aria-label="Floor plan of Suite 120"></div>
  <div class="photo plan plan--100" role="img" aria-label="Floor plan of Suite 100"></div>
  <div class="photo room--100" role="img" aria-label="Furnished meeting room in Suite 100 with conference table and arched window">
    <div class="caption">SUITE 100 - AVAILABLE IN FEBRUARY 2019</div>
  </div>

  <div class="abs spec-panel spec--100">
    <h3>SUITE 100</h3>
    <ul>
      <li>2,303 Sf</li>
      <li>6 Offices</li>
      <li>Break Room</li>
      <li>Reception Area</li>
      <li>Very Large Meeting Room</li>
      <li>Plenty of parking</li>
      <li>On-site management</li>
    </ul>
  </div>

  <div class="abs back-contact">
    For leasing information,<br>please contact:
    <div class="name">Dana Morrell</div>
    <div class="icon-line"><svg viewBox="0 0 10 10"><path d="M2 1l2 0 1 2-1.2 1a5 5 0 0 0 2.2 2.2L7 5l2 1v2a1 1 0 0 1-1 1A8 8 0 0 1 1 2a1 1 0 0 1 1-1z" fill="#666"/></svg>561-555-0148</div>
    <div class="icon-line"><svg viewBox="0 0 10 10"><rect x="0.5" y="2" width="9" height="6" fill="#666"/></svg>dana@norvalecompanies.com</div>
  </div>

  <div class="abs brand-name back-brand">
    <span class="big">Norvale</span><span class="small">Companies</span>
  </div>

  <div class="abs footer-rule"></div>
</section>

</body>
</html>
```